Criação de Layout Email Mkt/Newsletter para Construção & Engenharia
" Atualmente estamos iniciando a empresa, trabalhamos com as referências acima, somos dois sócios que trabalham com o mesmo objetivo, alguns serviços praticados por administração, projetos e construção com mão de obra propiá, estamos em processo de formação da empresa. "

```html
<!DOCTYPE html>
<html lang="pt-BR">
<head>
<meta charset="UTF-8">
<title>Vértice Engenharia — Newsletter</title>
<link rel="stylesheet" href="https://fonts.googleapis.com/css2?family=Montserrat:wght@400;500;600;700;800&display=swap">
<style>
  :root{
    --yellow:#f4b61d;
    --dark:#2a2c31;
    --ink:#3a3a3a;
    --muted:#6b6b6b;
    --panel:#f4f4f4;
    --white:#ffffff;
  }
  *{box-sizing:border-box;margin:0;padding:0}
  html,body{width:1200px;height:1200px;overflow:hidden;background:var(--white)}
  body{font-family:"Montserrat",sans-serif;color:var(--ink);position:relative}
  .newsletter{position:absolute;left:245px;top:0;width:710px;height:1200px;background:var(--white);overflow:hidden}
  .abs{position:absolute}

  /* hero */
  .hero{left:0;top:0;width:710px;height:403px;
    background:linear-gradient(160deg,#2f2a22 0%,#5a4a32 35%,#8a7350 55%,#3b3328 80%,#1e1c1a 100%)}
  .brand{left:0;top:95px;width:710px;text-align:center;color:var(--white)}
  .brand-name{font-size:62px;font-weight:700;letter-spacing:6px;line-height:1}
  .brand-sub{font-size:15px;font-weight:700;letter-spacing:9px;margin-top:14px}
  .tagline-frame{left:158px;top:262px;width:520px;height:74px;border:2px solid rgba(255,255,255,.8);border-right:none}
  .tagline{left:158px;top:252px;width:552px;text-align:center}
  .tagline-top{display:inline-block;background:rgba(40,36,30,.9);padding:0 14px;color:var(--white);font-size:21px;font-weight:500;letter-spacing:3px}
  .tagline-main{color:var(--yellow);font-size:38px;font-weight:800;letter-spacing:2px;margin-top:4px}

  /* intro */
  .intro{left:150px;top:430px;width:410px;text-align:center;font-size:12.5px;line-height:1.55;color:var(--muted)}
  .intro p+p{margin-top:14px}
  .intro strong{color:var(--ink)}

  /* services */
  .services-bg{left:0;top:571px;width:710px;height:440px;background:linear-gradient(90deg,#d8d6d0,#efeeeb)}
  .worker{left:0;top:571px;width:360px;height:440px;
    background:linear-gradient(170deg,#c9c4b8 0%,#b8ad98 30%,#b3342c 60%,#8e2622 100%)}
  .section-head-frame{left:238px;top:612px;width:324px;height:88px;border:2px solid var(--white)}
  .section-head{left:223px;top:600px;width:324px;height:88px;background:var(--yellow);color:var(--white);padding:20px 26px}
  .section-head h2{font-size:26px;font-weight:800;letter-spacing:1px;line-height:1}
  .section-head span{font-size:13px;font-weight:500;display:block;margin-top:6px}
  .card{left:360px;width:350px;background:var(--panel);padding:0 20px 0 22px;display:flex;gap:12px;color:var(--dark)}
  .card h3{font-size:14px;font-weight:700;line-height:1.25;letter-spacing:.5px}
  .card svg{flex:none}
  .card-plan{top:708px;height:56px;align-items:center}
  .card-projects{top:773px;height:170px;padding-top:16px}
  .card-manage{top:955px;height:50px;align-items:center}
  .service-list{list-style:none;display:grid;grid-template-columns:1fr 1fr;gap:7px 8px;margin-top:10px;font-size:11px;color:var(--ink)}
  .service-list li{display:flex;align-items:center;gap:6px;white-space:nowrap}
  .service-list li.wide{grid-column:1 / span 2}
  .cta{left:355px;top:1013px;width:325px;height:43px;background:var(--yellow);color:var(--white);font-size:11px;font-weight:700;letter-spacing:.5px;display:flex;align-items:center;justify-content:center}

  /* footer */
  .footer{left:0;top:1063px;width:710px;height:86px;background:var(--dark)}
  .logo-box{left:48px;top:1020px;width:163px;height:173px;background:var(--white);display:flex;flex-direction:column;align-items:center;justify-content:center;gap:6px;box-shadow:0 2px 8px rgba(0,0,0,.15)}
  .logo-name{font-size:25px;font-weight:700;color:var(--dark);letter-spacing:1px;line-height:1}
  .logo-sub{font-size:11px;font-weight:700;color:var(--dark);letter-spacing:3px;line-height:1}
  .contact{top:1078px;color:var(--white)}
  .contact h4{font-size:13px;font-weight:700;letter-spacing:.5px;margin-left:30px}
  .contact p{font-size:10.5px;line-height:1.35;margin:4px 0 0 30px;color:#e8e8e8}
  .contact small{color:var(--yellow);font-size:9px}
  .contact svg{position:absolute;left:0;top:0}
  .contact-phone{left:235px;width:215px}
  .contact-address{left:455px;width:250px}
  .web{left:0;top:1149px;width:710px;height:51px;display:flex;align-items:center;justify-content:center;font-size:15px;font-weight:700;color:var(--dark)}
</style>
</head>
<body>
<main class="newsletter">
  <header class="abs hero" role="img" aria-label="Foto de prédio em construção com guindaste ao entardecer"></header>
  <div class="abs brand">
    <div class="brand-name">VÉRTICE</div>
    <div class="brand-sub">ENGENHARIA</div>
  </div>
  <div class="abs tagline-frame"></div>
  <div class="abs tagline">
    <div class="tagline-top">SEU SONHO, SEU OBJETIVO</div>
    <div class="tagline-main">A GENTE CONSTRÓI</div>
  </div>

  <section class="abs intro">
    <p>A administração de uma obra envolve o controle completo dos custos, prazos e da qualidade dos serviços.</p>
    <p><strong>VÉRTICE ENGENHARIA</strong> utiliza módulos que permitem o acompanhamento de cada etapa de sua obra com a máxima precisão, evitando imprevistos que comprometam os seus resultados.</p>
  </section>

  <div class="abs services-bg"></div>
  <div class="abs worker" role="img" aria-label="Foto de engenheiro sorridente de capacete amarelo e jaqueta vermelha segurando uma prancheta"></div>
  <div class="abs section-head-frame"></div>
  <div class="abs section-head"><h2>O QUE FAZEMOS</h2><span>nossas soluções</span></div>

  <div class="abs card card-plan">
    <svg width="24" height="24" viewBox="0 0 24 24"><circle cx="7" cy="6" r="3" fill="#2a2c31"/><path d="M3 22v-8a4 4 0 0 1 8 0v8z" fill="#2a2c31"/><rect x="13" y="12" width="9" height="10" fill="#2a2c31"/></svg>
    <h3>PLANEJAMENTO E<br>ORÇAMENTO DE OBRAS</h3>
  </div>

  <div class="abs card card-projects">
    <svg width="22" height="24" viewBox="0 0 22 24"><rect x="2" y="2" width="18" height="20" fill="none" stroke="#2a2c31" stroke-width="2"/><rect x="6" y="7" width="10" height="2" fill="#2a2c31"/><rect x="6" y="12" width="10" height="2" fill="#2a2c31"/></svg>
    <div>
      <h3>PROJETOS E SERVIÇOS</h3>
      <ul class="service-list">
        <li><svg width="11" height="9" viewBox="0 0 11 9"><path d="M1 5l3 3 6-7" fill="none" stroke="#f4b61d" stroke-width="2"/></svg>Topografia</li>
        <li><svg width="11" height="9" viewBox="0 0 11 9"><path d="M1 5l3 3 6-7" fill="none" stroke="#f4b61d" stroke-width="2"/></svg>Arquitetônicos</li>
        <li><svg width="11" height="9" viewBox="0 0 11 9"><path d="M1 5l3 3 6-7" fill="none" stroke="#f4b61d" stroke-width="2"/></svg>Estudo do solo</li>
        <li><svg width="11" height="9" viewBox="0 0 11 9"><path d="M1 5l3 3 6-7" fill="none" stroke="#f4b61d" stroke-width="2"/></svg>Fundação</li>
        <li><svg width="11" height="9" viewBox="0 0 11 9"><path d="M1 5l3 3 6-7" fill="none" stroke="#f4b61d" stroke-width="2"/></svg>Estruturas</li>
        <li><svg width="11" height="9" viewBox="0 0 11 9"><path d="M1 5l3 3 6-7" fill="none" stroke="#f4b61d" stroke-width="2"/></svg>Instalações</li>
        <li class="wide"><svg width="11" height="9" viewBox="0 0 11 9"><path d="M1 5l3 3 6-7" fill="none" stroke="#f4b61d" stroke-width="2"/></svg>Combate incêndio</li>
        <li class="wide"><svg width="11" height="9" viewBox="0 0 11 9"><path d="M1 5l3 3 6-7" fill="none" stroke="#f4b61d" stroke-width="2"/></svg>Perspectivas internas e externas 3D</li>
        <li><svg width="11" height="9" viewBox="0 0 11 9"><path d="M1 5l3 3 6-7" fill="none" stroke="#f4b61d" stroke-width="2"/></svg>Moveis planejados</li>
        <li><svg width="11" height="9" viewBox="0 0 11 9"><path d="M1 5l3 3 6-7" fill="none" stroke="#f4b61d" stroke-width="2"/></svg>Vidraçaria</li>
      </ul>
    </div>
  </div>

  <div class="abs card card-manage">
    <svg width="24" height="22" viewBox="0 0 24 22"><circle cx="12" cy="5" r="4" fill="#2a2c31"/><path d="M3 22a9 9 0 0 1 18 0z" fill="#2a2c31"/></svg>
    <h3>GESTÃO DE OBRAS<br>CONSULTORIA</h3>
  </div>

  <a class="abs cta">CLIQUE AQUI E VEJA TODOS OS DETALHES</a>

  <footer class="abs footer"></footer>
  <div class="abs logo-box"><span class="logo-name">VÉRTICE</span><span class="logo-sub">ENGENHARIA</span></div>

  <div class="abs contact contact-phone">
    <svg width="22" height="22" viewBox="0 0 22 22"><circle cx="11" cy="11" r="11" fill="#ffffff"/><path d="M7 6c1 0 2 2 2 3l-1 1c.6 1.4 1.6 2.4 3 3l1-1c1 0 3 1 3 2s-1 2-2 2c-4 0-8-4-8-8 0-1 1-2 2-2z" fill="#2a2c31"/></svg>
    <h4>TELEFONES</h4>
    <p>(31) 90000-1234 / 90000-5678<br><small>*Linha 1 &nbsp;&nbsp;&nbsp;&nbsp;&nbsp; *Linha 2</small></p>
  </div>
  <div class="abs contact contact-address">
    <svg width="22" height="22" viewBox="0 0 22 22"><circle cx="11" cy="11" r="11" fill="#ffffff"/><path d="M11 4a5 5 0 0 0-5 5c0 4 5 9 5 9s5-5 5-9a5 5 0 0 0-5-5zm0 7a2 2 0 1 1 0-4 2 2 0 0 1 0 4z" fill="#2a2c31"/></svg>
    <h4>ENDEREÇO MATRIZ</h4>
    <p>Rua das Acácias, Nº 120<br>Contagem, Minas Gerais</p>
  </div>

  <div class="abs web">www.verticeeng.com</div>
</main>
</body>
</html>
```